New Corporate website more focused on funnel and great design

Our company, Bold Harbor needs a new website to look like it's from 2021. We work with large businesses in the corporte world and need to reflect that we are professional, focused on our clients, and trsutworthy. It should include some/most of the components from our current site: boldharbor.com but should focus more about getting people to optin to out free downloads, which can be found on this page: https://www.boldharbor.com/get-started-with-a-prep-session/ and this page: https://www.boldharbor.com/team-onboarding/

Our new website should do a better job at explaining what we do, who we serve, and how we fix their problems of onboarding new leaders. Feel free to use dummy text if you are not sure what to put in for certain sections. I also would like to point out that most of the audiance is older, so we don't need anything too younge and flashy, or that is hard it use. it should have big clear fonts, plently of contrast, and work well for poeple who are not good at using the internet. Please use the colors of the logo, and you can add another color or two if you think it's fits

Industry/Entity Type

business consulting

Number of Pages Required

2 page

Font styles to use
Sans Serif

Requirements
Must have
• corporate feel, look professional, focus on getting new leads
Should not have
• cute or children feel

```html
<!DOCTYPE html>
<html lang="en">
<head>
<meta charset="utf-8">
<title>Bold Harbor — Accelerate Business Performance</title>
<link rel="stylesheet" href="https://fonts.googleapis.com/css2?family=Roboto:wght@400;500;700;900&display=swap">
<style>
:root{
  --blue:#1b5193;
  --blue-dark:#174377;
  --ink:#1d1d1f;
  --text:#6b6b6b;
  --line:#d9dde3;
  --band:#3b3d40;
  --white:#fff;
}
*{box-sizing:border-box;margin:0;padding:0}
html,body{width:1200px;height:4289px;overflow:hidden}
body{font-family:"Roboto",Arial,sans-serif;color:var(--ink);background:#fff;position:relative}
a{color:inherit;text-decoration:none}
.abs{position:absolute}
.btn{position:absolute;display:flex;align-items:center;justify-content:center;gap:10px;background:var(--blue);color:#fff;font-weight:700;font-size:14px;letter-spacing:.2px;border-radius:2px}
.btn svg{width:14px;height:14px}

/* header */
.site-header{position:absolute;left:0;top:0;width:1200px;height:72px;background:#fff}
.brand{position:absolute;left:111px;top:16px;display:flex;align-items:center;gap:10px}
.brand-square{width:36px;height:36px;background:var(--blue)}
.brand-name{font-size:28px;font-weight:500;color:var(--blue-dark)}
.main-nav{position:absolute;left:431px;top:27px;display:flex;gap:25px;font-size:13px;font-weight:700}
.main-nav a.active{color:var(--blue)}
.login{left:978px;top:15px;width:109px;height:40px;font-size:13px}

/* hero */
.hero{position:absolute;left:0;top:72px;width:1200px;height:554px;background:linear-gradient(100deg,#5d6a6c 0%,#8a9590 35%,#b7c2c6 60%,#d3dbe0 100%)}
.hero-title{position:absolute;left:111px;top:126px;width:460px;color:#fff;font-size:45px;line-height:52px;font-weight:700}
.hero .btn{left:111px;top:369px;width:155px;height:47px}

/* who we are */
.wwa-frame{left:223px;top:727px;width:355px;height:422px;border:3px solid var(--blue)}
.wwa-photo{left:110px;top:752px;width:445px;height:374px;background:linear-gradient(135deg,#b9c0c6,#7d8790 55%,#4b5560)}
.h2{font-size:31px;font-weight:700;color:var(--ink)}
.wwa-title{left:651px;top:743px}
.body-copy{font-size:14px;line-height:25.6px;color:var(--text)}
.wwa-copy{left:651px;top:800px;width:440px}
.wwa-btn{left:651px;top:1083px;width:236px;height:47px}

/* what we do */
.wwd{position:absolute;left:0;top:1266px;width:1200px;height:525px}
.wwd-bg{position:absolute;inset:0}
.wwd-title{position:absolute;left:0;width:1200px;top:70px;text-align:center;color:#fff;font-size:30px;font-weight:500}
.service{position:absolute;top:158px;width:213px;height:243px;background:rgba(255,255,255,.55);padding:11px}
.service-inner{width:100%;height:100%;background:#fff;border:2px solid var(--blue);text-align:center;padding:12px 14px 0;overflow:hidden}
.service-icon{width:62px;height:62px;border-radius:50%;margin:0 auto;display:block}
.service-name{font-size:12px;font-weight:700;margin-top:22px}
.service-text{font-size:12px;line-height:20px;color:var(--text);margin-top:18px;height:60px;overflow:hidden}

/* who we serve */
.wws-title{left:110px;top:1900px}
.wws-copy{left:110px;top:1955px;width:420px;text-align:justify}
.wws-btn{left:110px;top:2238px;width:158px;height:47px}
.wws-frame{left:587px;top:1884px;width:358px;height:423px;border:3px solid var(--blue)}
.wws-gallery{left:600px;top:1897px;width:504px;height:396px;background:#fff}
.ph-a{left:612px;top:1907px;width:269px;height:374px;background:linear-gradient(150deg,#e5e7e6,#aab1b6 55%,#6f6a62)}
.ph-b{left:890px;top:1907px;width:201px;height:180px;background:linear-gradient(140deg,#9a8373,#c7b4a2 50%,#6d5a4e)}
.ph-c{left:890px;top:2095px;width:201px;height:186px;background:linear-gradient(140deg,#d8d8d6,#8f8b86 50%,#4e4c4a)}

/* how we fix */
.fix-band{position:absolute;left:0;top:2438px;width:1200px;height:316px;background:linear-gradient(180deg,#333537,#55585b)}
.fix-title{position:absolute;left:0;width:1200px;top:2495px;text-align:center;color:#fff;font-size:30px;font-weight:500}
.fix-sub{position:absolute;left:220px;width:760px;top:2550px;text-align:center;color:#fff;font-size:14px;line-height:23px}
.fix-card{position:absolute;top:2642px;width:320px;height:295px;background:#fff;box-shadow:0 2px 10px rgba(0,0,0,.14);text-align:center;overflow:hidden}
.fix-card.featured{border-bottom:3px solid var(--blue)}
.fix-icon{position:absolute;left:98px;top:-62px;width:124px;height:124px;border-radius:50%;background:#efefef}
.fix-card.featured .fix-icon{background:var(--blue)}
.fix-icon svg{position:absolute;left:42px;top:66px;width:40px;height:48px}
.fix-name{margin-top:102px;font-size:14px;font-weight:700}
.fix-text{margin:38px auto 0;width:282px;font-size:14px;line-height:23px;color:var(--text)}
.fix-more{display:inline-flex;align-items:center;gap:8px;margin-top:18px;color:var(--blue);font-size:12px;font-weight:700;text-decoration:underline}
.fix-more svg{width:12px;height:12px}

/* testimonials */
.tst-title{left:0;width:1200px;top:3030px;text-align:center;font-size:35px;font-weight:500}
.tst{position:absolute;top:3123px;width:300px}
.avatar{position:absolute;left:0;top:0;width:57px;height:57px;border-radius:50%;background:linear-gradient(160deg,#c9ced4,#5d6570)}
.tst-name{position:absolute;left:83px;top:10px;font-size:14px;font-weight:500;color:#444}
.tst-role{position:absolute;left:83px;top:31px;font-size:14px;color:var(--text)}
.tst-quote{position:absolute;left:0;top:76px;width:300px;font-size:14px;line-height:25.6px;color:var(--text)}
.tst-nav{position:absolute;top:3339px;width:22px;height:24px}

/* contact */
.contact-title{left:0;width:1200px;top:3448px;text-align:center;font-size:31px;font-weight:500}
.contact-bg{position:absolute;left:0;top:3686px;width:1200px;height:603px}
.form-card{position:absolute;left:185px;top:3523px;width:831px;height:372px;background:#fff;border-top:4px solid var(--blue)}
.field{position:absolute;height:45px;border:1px solid var(--line);font-size:14px;color:#777;padding:13px 17px}
.field.msg{height:101px}
.submit{left:596px;top:3804px;width:158px;height:46px}

/* footer */
.foot-h{position:absolute;top:3952px;color:#fff;font-size:14px;font-weight:700;text-decoration:underline}
.foot-list{position:absolute;top:3987px;list-style:none;color:#fff;font-size:14px}
.foot-list li{height:37px;display:flex;align-items:flex-start;gap:14px}
.foot-list svg{width:12px;height:14px;margin-top:2px;flex:none}
.contact-list li{height:auto;margin-bottom:14px;line-height:26px}
.contact-list li svg{margin-top:6px}
.news{position:absolute;left:794px;top:3997px;width:288px;height:47px;background:#fff;border:1px solid #cfd5dd;display:flex}
.news span{flex:1;padding:15px 17px;font-size:14px;color:#777}
.news b{width:47px;background:var(--blue);display:flex;align-items:center;justify-content:center}
.foot-rule{position:absolute;left:118px;top:4203px;width:964px;height:1px;background:rgba(255,255,255,.35)}
.copyright{position:absolute;left:0;width:1200px;top:4231px;text-align:center;color:#fff;font-size:14px}
</style>
</head>
<body>

<header class="site-header">
  <a class="brand" href="#"><span class="brand-square"></span><span class="brand-name">Bold Harbor</span></a>
  <nav class="main-nav">
    <a class="active" href="#">HOME</a><a href="#">WHO WE ARE</a><a href="#">WHAT WE DO</a><a href="#">CLIENTS</a><a href="#">BLOG</a><a href="#">CONTACT</a>
  </nav>
  <a class="btn login" href="#">LOG IN
    <svg viewBox="0 0 14 14"><rect x="3" y="6" width="8" height="7" fill="#fff"/><path d="M4.5 6V4a2.5 2.5 0 0 1 5 0v2" stroke="#fff" stroke-width="1.6" fill="none"/></svg></a>
</header>

<section class="hero" role="img" aria-label="Business leaders in a bright modern office reviewing documents together">
  <h1 class="hero-title">Accelerate Business Performance During Critical Leadership Transitions</h1>
  <a class="btn" href="#">GET STARTED
    <svg viewBox="0 0 14 14"><circle cx="7" cy="7" r="7" fill="#fff"/><path d="M5.5 4l3 3-3 3" stroke="#1b5193" stroke-width="1.8" fill="none"/></svg></a>
</section>

<!-- who we are -->
<div class="abs wwa-frame"></div>
<div class="abs wwa-photo" role="img" aria-label="Three colleagues in business attire talking in an office"></div>
<h2 class="abs h2 wwa-title">Who We Are</h2>
<div class="abs body-copy wwa-copy">
  <p>We know, through our personal experiences gained as leaders, that the first 100 days in a critical transition are a crucible of leadership – when managed well, leaders build cohesive teams that succeed. When managed poorly, leaders falter, teams stall, and organizations fail.</p>
  <p>These experiences, and our motivation to make things better for leaders during critical transitions, became the initial catalyst for the creation of the tools that became the core of the Bold Harbor approach to our executive onboarding services and the foundation of our first book, The First Hundred Days Field Guide.</p>
</div>
<a class="btn wwa-btn" href="#">LEARN MORE ABOUT US
  <svg viewBox="0 0 14 14"><circle cx="7" cy="7" r="7" fill="#fff"/><path d="M5.5 4l3 3-3 3" stroke="#1b5193" stroke-width="1.8" fill="none"/></svg></a>

<!-- what we do -->
<section class="wwd">
  <svg class="wwd-bg" viewBox="0 0 1200 525" preserveAspectRatio="none" role="img" aria-label="Blue tinted photo of a team at work">
    <defs><linearGradient id="wwdGrad" x1="0" x2="1" y1="0" y2="1"><stop offset="0" stop-color="#2563a6"/><stop offset=".55" stop-color="#1e5798"/><stop offset="1" stop-color="#184a86"/></linearGradient></defs>
    <path d="M175 0H1200V525H195C70 525 0 420 0 265C0 110 60 0 175 0Z" fill="url(#wwdGrad)"/>
  </svg>
  <h2 class="wwd-title">What We Do</h2>

  <div class="service" style="left:153px"><div class="service-inner">
    <svg class="service-icon" viewBox="0 0 62 62"><circle cx="31" cy="31" r="31" fill="#dfe6ef"/><circle cx="31" cy="31" r="24" fill="var(--blue)"/><path d="M20 32l7-6 8 4 7-5v9l-8 5-14-7z" fill="#fff"/></svg>
    <div class="service-name">EXECUTIVE ONBOARDING</div>
    <div class="service-text">For executive leaders taking on new roles, the Bold Harbor 100-Day approach to your first steps</div>
  </div></div>

  <div class="service" style="left:381px"><div class="service-inner">
    <svg class="service-icon" viewBox="0 0 62 62"><circle cx="31" cy="31" r="31" fill="#e3e3e3"/><circle cx="31" cy="31" r="24" fill="#555"/><circle cx="31" cy="31" r="10" fill="none" stroke="#fff" stroke-width="3"/><circle cx="31" cy="31" r="3" fill="#fff"/></svg>
    <div class="service-name">TEAM ONBOARDING</div>
    <div class="service-text">For leaders integrating teams post acquisition or re-organization, the path to alignment</div>
  </div></div>

  <div class="service" style="left:607px"><div class="service-inner">
    <svg class="service-icon" viewBox="0 0 62 62"><circle cx="31" cy="31" r="31" fill="#dfe6ef"/><circle cx="31" cy="31" r="24" fill="var(--blue)"/><path d="M22 40l14-14M30 24h8v8" stroke="#fff" stroke-width="3" fill="none"/></svg>
    <div class="service-name">ACCELERATION</div>
    <div class="service-text">For executives leading through a strategic point of inflection</div>
  </div></div>

  <div class="service" style="left:834px"><div class="service-inner">
    <svg class="service-icon" viewBox="0 0 62 62"><circle cx="31" cy="31" r="31" fill="#e3e3e3"/><circle cx="31" cy="31" r="24" fill="#555"/><rect x="24" y="20" width="14" height="20" fill="#fff"/><path d="M27 26h8M27 30h8M27 34h5" stroke="#555" stroke-width="1.6"/></svg>
    <div class="service-name">CASE STUDIES</div>
    <div class="service-text">For executives leading through a strategic point of inflection</div>
  </div></div>
</section>

<!-- who we serve -->
<h2 class="abs h2 wws-title">Who We Serve</h2>
<p class="abs body-copy wws-copy">At vero eos et accusamus et iusto odio dignissimos ducimus qui blanditiis praesentium voluptatum deleniti atque corrupti quos dolores et quas molestias excepturi sint occaecati cupiditate non provident, similique sunt in culpa qui officia deserunt mollitia animi, id est laborum et dolorum fuga. Et harum quidem rerum facilis est et expedita distinctio. Nam libero tempore, cum soluta nobis est eligendi optio cumque nihil impedit quo minus id quod maxime placeat facere possimus, omnis voluptas assumenda est, omnis dolor repellendus. Temporibus autem quibusdam et aut officiis debitis aut rerum necessitatibus</p>
<a class="btn wws-btn" href="#">LEARN MORE
  <svg viewBox="0 0 14 14"><circle cx="7" cy="7" r="7" fill="#fff"/><path d="M5.5 4l3 3-3 3" stroke="#1b5193" stroke-width="1.8" fill="none"/></svg></a>
<div class="abs wws-frame"></div>
<div class="abs wws-gallery"></div>
<div class="abs ph-a" role="img" aria-label="Presenter writing on a whiteboard for colleagues"></div>
<div class="abs ph-b" role="img" aria-label="Team of colleagues gathered around a laptop"></div>
<div class="abs ph-c" role="img" aria-label="Group meeting around a table in an office"></div>

<!-- how we fix -->
<div class="fix-band" role="img" aria-label="Dark toned photo of a city skyline"></div>
<h2 class="fix-title">How We Fix Their Problems</h2>
<p class="fix-sub">Lorem ipsum dolor sit amet, consectetur adipiscing elit, sed do eiusmod tempor incididunt ut labore et dolore magna aliqua. Ut enim ad minim veniam, quis nostrud exercitation ullamco laboris nisi ut aliquip</p>

<div class="fix-card" style="left:101px">
  <div class="fix-icon"><svg viewBox="0 0 40 48"><circle cx="10" cy="8" r="4" fill="#1b5193"/><circle cx="20" cy="6" r="4" fill="#1b5193"/><circle cx="30" cy="8" r="4" fill="#1b5193"/><rect x="4" y="16" width="32" height="4" fill="#1b5193"/><path d="M8 20v14M32 20v14M20 20v14" stroke="#1b5193" stroke-width="3"/></svg></div>
  <div class="fix-name">NEMO ENIM IPSAM VOLUPTATEM</div>
  <p class="fix-text">Lorem ipsum dolor sit amet, consectetur adipiscing elit, sed do eiusmod teincididunt ut labore et dolore magna</p>
  <a class="fix-more" href="#">LEARN MORE <svg viewBox="0 0 14 14"><circle cx="7" cy="7" r="7" fill="#1b5193"/><path d="M5.5 4l3 3-3 3" stroke="#fff" stroke-width="1.8" fill="none"/></svg></a>
</div>

<div class="fix-card featured" style="left:441px">
  <div class="fix-icon"><svg viewBox="0 0 40 48"><circle cx="20" cy="10" r="7" fill="none" stroke="#fff" stroke-width="2.5"/><path d="M6 36c2-10 26-10 28 0" stroke="#fff" stroke-width="2.5" fill="none"/><circle cx="30" cy="26" r="5" fill="none" stroke="#fff" stroke-width="2"/></svg></div>
  <div class="fix-name">NEMO ENIM IPSAM VOLUPTATEM</div>
  <p class="fix-text">Lorem ipsum dolor sit amet, consectetur adipiscing elit, sed do eiusmod teincididunt ut labore et dolore magna</p>
  <a class="fix-more" href="#">LEARN MORE <svg viewBox="0 0 14 14"><circle cx="7" cy="7" r="7" fill="#1b5193"/><path d="M5.5 4l3 3-3 3" stroke="#fff" stroke-width="1.8" fill="none"/></svg></a>
</div>

<div class="fix-card" style="left:779px">
  <div class="fix-icon"><svg viewBox="0 0 40 48"><rect x="14" y="2" width="22" height="14" fill="#1b5193"/><circle cx="8" cy="12" r="4" fill="#1b5193"/><path d="M4 20h8v12M2 32h36" stroke="#1b5193" stroke-width="3" fill="none"/></svg></div>
  <div class="fix-name">NEMO ENIM IPSAM VOLUPTATEM</div>
  <p class="fix-text">Lorem ipsum dolor sit amet, consectetur adipiscing elit, sed do eiusmod teincididunt ut labore et dolore magna</p>
  <a class="fix-more" href="#">LEARN MORE <svg viewBox="0 0 14 14"><circle cx="7" cy="7" r="7" fill="#1b5193"/><path d="M5.5 4l3 3-3 3" stroke="#fff" stroke-width="1.8" fill="none"/></svg></a>
</div>

<!-- testimonials -->
<h2 class="abs tst-title">What our clients say</h2>
<div class="tst" style="left:115px">
  <div class="avatar" role="img" aria-label="Client portrait"></div>
  <div class="tst-name">DANIEL ASHFORD</div><div class="tst-role">Businessman</div>
  <p class="tst-quote">“&nbsp; Lorem ipsum dolor sit amet, consectetur adipiscing elit, sed do eiusmod tempor incididunt ut labore et dolore &nbsp;”</p>
</div>
<div class="tst" style="left:458px">
  <div class="avatar" role="img" aria-label="Client portrait"></div>
  <div class="tst-name">DANIEL ASHFORD</div><div class="tst-role">Businessman</div>
  <p class="tst-quote">“&nbsp; Lorem ipsum dolor sit amet, consectetur adipiscing elit, sed do eiusmod tempor incididunt ut labore et dolore &nbsp;”</p>
</div>
<div class="tst" style="left:799px">
  <div class="avatar" role="img" aria-label="Client portrait"></div>
  <div class="tst-name">DANIEL ASHFORD</div><div class="tst-role">Businessman</div>
  <p class="tst-quote">“&nbsp; Lorem ipsum dolor sit amet, consectetur adipiscing elit, sed do eiusmod tempor incididunt ut labore et dolore &nbsp;”</p>
</div>
<svg class="tst-nav" style="left:565px" viewBox="0 0 22 24"><path d="M14 5l-7 7 7 7" stroke="#222" stroke-width="2.2" fill="none"/></svg>
<svg class="tst-nav" style="left:617px" viewBox="0 0 22 24"><path d="M8 5l7 7-7 7" stroke="#222" stroke-width="2.2" fill="none"/></svg>

<!-- contact -->
<svg class="contact-bg" viewBox="0 0 1200 603" preserveAspectRatio="none">
  <path d="M0 0C150 60 240 90 330 95H860C960 90 1080 60 1200 66V603H0Z" fill="var(--blue-dark)"/>
</svg>
<h2 class="abs contact-title">Speak to One of Our Partners Today</h2>
<div class="form-card"></div>
<div class="field" style="left:216px;top:3566px;width:345px">First Name</div>
<div class="field" style="left:216px;top:3622px;width:345px">Last Name</div>
<div class="field" style="left:216px;top:3677px;width:345px">Phone No</div>
<div class="field" style="left:216px;top:3734px;width:345px">Subject</div>
<div class="field" style="left:216px;top:3789px;width:345px">Email</div>
<div class="field" style="left:596px;top:3566px;width:388px">Address</div>
<div class="field" style="left:596px;top:3622px;width:388px">Zip Code</div>
<div class="field msg" style="left:596px;top:3677px;width:388px">Message</div>
<a class="btn submit" href="#">SUBMIT NOW
  <svg viewBox="0 0 14 14"><circle cx="7" cy="7" r="7" fill="#fff"/><path d="M5.5 4l3 3-3 3" stroke="#1b5193" stroke-width="1.8" fill="none"/></svg></a>

<!-- footer -->
<footer>
  <div class="foot-h" style="left:118px">OPTIMIZE</div>
  <ul class="foot-list contact-list" style="left:118px;width:250px">
    <li><svg viewBox="0 0 12 14"><path d="M6 0a4.5 4.5 0 0 1 4.5 4.5C10.5 8 6 14 6 14S1.5 8 1.5 4.5A4.5 4.5 0 0 1 6 0z" fill="#fff"/><circle cx="6" cy="4.5" r="1.6" fill="#174377"/></svg><span>12/48 Harbour Crescent<br>Marlow Bay QLD 4310</span></li>
    <li><svg viewBox="0 0 12 14"><path d="M2 1l3 0 1 3-2 1.5c.8 1.8 2 3 3.8 3.8L9.3 7.3l3 1V11c-6 .5-11-4.5-10.3-10z" fill="#fff"/></svg><span>+1 555.014.2270<br>+44 (0) 7700 900418</span></li>
    <li><svg viewBox="0 0 12 14"><rect x="0" y="3" width="12" height="9" fill="#fff"/><path d="M0 3l6 5 6-5" stroke="#174377" stroke-width="1.2" fill="none"/></svg><span>info@boldharbor.com</span></li>
  </ul>

  <div class="foot-h" style="left:401px">QUICK LINKS</div>
  <ul class="foot-list" style="left:401px">
    <li><svg viewBox="0 0 12 14"><path d="M2 3l4 4-4 4M6 3l4 4-4 4" stroke="#fff" stroke-width="1.6" fill="none"/></svg>Home</li>
    <li><svg viewBox="0 0 12 14"><path d="M2 3l4 4-4 4M6 3l4 4-4 4" stroke="#fff" stroke-width="1.6" fill="none"/></svg>About Us</li>
    <li><svg viewBox="0 0 12 14"><path d="M2 3l4 4-4 4M6 3l4 4-4 4" stroke="#fff" stroke-width="1.6" fill="none"/></svg>Our Services</li>
    <li><svg viewBox="0 0 12 14"><path d="M2 3l4 4-4 4M6 3l4 4-4 4" stroke="#fff" stroke-width="1.6" fill="none"/></svg>Resources</li>
    <li><svg viewBox="0 0 12 14"><path d="M2 3l4 4-4 4M6 3l4 4-4 4" stroke="#fff" stroke-width="1.6" fill="none"/></svg>Testimonials</li>
  </ul>

  <div class="foot-h" style="left:586px">OTHER LINKS</div>
  <ul class="foot-list" style="left:586px">
    <li><svg viewBox="0 0 12 14"><path d="M2 3l4 4-4 4M6 3l4 4-4 4" stroke="#fff" stroke-width="1.6" fill="none"/></svg>Terms &amp; Conditions</li>
    <li><svg viewBox="0 0 12 14"><path d="M2 3l4 4-4 4M6 3l4 4-4 4" stroke="#fff" stroke-width="1.6" fill="none"/></svg>Privacy Policy</li>
    <li><svg viewBox="0 0 12 14"><path d="M2 3l4 4-4 4M6 3l4 4-4 4" stroke="#fff" stroke-width="1.6" fill="none"/></svg>Help Service</li>
    <li><svg viewBox="0 0 12 14"><path d="M2 3l4 4-4 4M6 3l4 4-4 4" stroke="#fff" stroke-width="1.6" fill="none"/></svg>FAQ</li>
    <li><svg viewBox="0 0 12 14"><path d="M2 3l4 4-4 4M6 3l4 4-4 4" stroke="#fff" stroke-width="1.6" fill="none"/></svg>Contact us</li>
  </ul>

  <div class="foot-h" style="left:794px;top:3950px">SUBSCRIBE TO OUR NEWSLETTER</div>
  <div class="news"><span>Email Address</span><b><svg width="18" height="18" viewBox="0 0 18 18"><path d="M17 1L1 8l7 2 2 7z" fill="#fff"/></svg></b></div>

  <div class="foot-rule"></div>
  <p class="copyright">© 2021 Bold Harbor. All Rights Reserved</p>
</footer>

</body>
</html>
```